One of Australia's fastest growing energy maintenance contractors needs a new website

www.panelbrite.com.au
Our business has evolved over the past years and now our website is no longer relevant.
We clean solar panels and we vacuum roof gutters.
We clean solar panels on the roofs of residential houses right up to billion dollar solar farms with in excess of 1 million panels. We offer thermal image testing and bird proofing for our residential and commercial clients and thermal drone imaging services for our solar farm clients.
We vacuum clean roof gutters (using a LoftSuk) on the residential house next door right up to enormous private and public schools, colleges, shopping centres, strat complexes and commercial buildings.
When first built our business had more of a domestic residential skew and the website reflected that. While that is still part of our core business we are now bidding on and have secured large government, commercial and infrastructure contracts and our new website needs to reflect our growth and our new business. We need a new site that it optimised for both desktop ad phone viewing as our latest figures showed that 73% of people visiting our site are on mobile phones. We have an extensive amount of data on Trekmetrics available as well as Bidlinks. Both that would also need integrating with the site along with a few other plugins such as Kembo Chat IQ, Friendwall etc along with SEO key words etc. We are also the winner and finalists over multiple years of the small business of the year awards and we like to proudly and prominently display those on our site.
We are looking for a new site with a modern professional feel / theme
There is a definitive break in our business between the solar Panel cleaning clients and the gutter cleaning clients so we would like a home page that begins with a simple choice:
Solar Panel Cleaning – Gutter Cleaning
With a professional full screen background image (we have hundreds to choose from) and along the bottom a small area with rights reserved etc, phone number etc (at some point in the future we will split these into two businesses but for now it’s what we have).
After that selection is made we would like a repeat of that same scenario but the selection is:
If it’s Solar Panel Cleaning
(new background image)
Government – Infrastructure – Commercial – Residential
If it’s Gutter Cleaning
(new background image)
Government – Strata – Commercial – Residential
After making those choices then onto the relevant pages with background images relevant to each sector and a them that suits (on the residential we would like to keep the link to our trekmetrics reviews) - We will provide copy / text for each relevant page.
Other than that, a menu inclusive of the above and:
Resellers Portal – we will provide a link to this from Kembo CRM)
Customer portal (we will supply a link to this from our booking system)
We also need a page for our Solar Resellers / Partners page but we will give them a link to this, it won’t be listed on the site.
Request a quote page (Again we will provide information from Kembo as this will be linked to the CRM)
Standard contact us page inclusive of phone numbers, address and fields supplied from CRM
Sydney – 02 7391 5084
Southern Highlands – 02 4863 1507
Goulburn – 02 4863 1507
Canberra – 02 6178 3045
Wollongong – 02 4239 7615
sales@panelbrite.com.au
Head Office - Ferndell NSW 2583
ABN: 48762093115
Responsive Design: Optimized for desktop and mobile (73% mobile visitors).
Fast Loading Speed: Optimized for performance.
Smooth Transition Animations: For service and category selection.
Sticky Contact Bar: Always accessible at the bottom of mobile screens for quick calls.
SEO Optimization: Focused on government tenders, large-scale commercial contracts, and infrastructure projects.
Integrations
Trekmetrics & Trekmetrics Bidlinks.
Kembo Chat IQ.
Friendwall Beacon.
SEO tools and keyword optimization.
Many many more images available if needed

```html
<!DOCTYPE html>
<html lang="en">
<head>
<meta charset="utf-8">
<title>PanelBrite – Website Screens</title>
<link href="https://fonts.googleapis.com/css2?family=Fira+Sans:wght@400;500;600;700&family=Quicksand:wght@500;600&family=Noto+Serif:wght@400&display=swap" rel="stylesheet">
<style>
:root{
  --board:#b3b3b3;
  --white:#ffffff;
  --footer:#052329;
  --accent:#1da1dd;
  --brand:#0f6fb5;
  --tile-dark:#0a6aaf;
  --tile-light:#33b1e5;
  --link:#37d0e0;
  --rule:#5d7378;
}
*{box-sizing:border-box;margin:0;padding:0}
html,body{width:1200px;height:2923px;overflow:hidden;background:var(--board);font-family:"Fira Sans",sans-serif}
.screen{position:absolute;left:167px;width:866px;height:852px;background:var(--white);overflow:hidden}
.screen--choice{top:111px}
.screen--solar{top:1016px}
.screen--gutter{top:1952px}
.hero{position:absolute;left:0;top:87px;width:866px;height:356px}
.site-header{position:absolute;left:0;top:0;width:866px;height:87px;background:var(--white);z-index:2}
.portal-btn{position:absolute;height:24px;width:115px;background:var(--accent);color:var(--white);font-size:11.5px;font-weight:500;display:flex;align-items:center;justify-content:center}
.portal-btn--resellers{left:80px;top:36px}
.portal-btn--customers{left:667px;top:32px}
.brand-badge{position:absolute;left:355px;top:-20px;width:156px;height:156px;border-radius:50%;background:var(--white);z-index:3;display:flex;flex-direction:column;align-items:center;justify-content:flex-end;padding-bottom:34px}
.brand-badge .dot{width:34px;height:34px;border-radius:50%;background:var(--brand);margin-bottom:10px}
.brand-name{font-family:"Quicksand",sans-serif;font-weight:600;font-size:23px;color:var(--brand)}
.choice-label{position:absolute;top:401px;height:52px;background:var(--white);color:var(--footer);font-size:25px;font-weight:600;display:flex;align-items:center;justify-content:center;border-radius:3px}
.choice-label--solar{left:88px;width:273px}
.choice-label--gutter{left:497px;width:276px}
.hero-copy{position:absolute;left:0;width:866px;text-align:center;color:var(--white);font-weight:600;text-shadow:0 1px 3px rgba(0,0,0,.55)}
.hero-copy--title{top:256px;font-size:20px}
.hero-copy--tagline{top:297px;font-size:20px;font-weight:700}
.sector-tile{position:absolute;top:397px;width:155px;height:101px;border-radius:8px;color:var(--white);display:flex;flex-direction:column;align-items:center;justify-content:center;gap:8px;font-size:20px;font-weight:600;box-shadow:0 2px 6px rgba(0,0,0,.3)}
.sector-tile svg{width:38px;height:38px}
.sector-tile--dark{background:var(--tile-dark)}
.sector-tile--light{background:var(--tile-light)}
.t1{left:73px}.t2{left:262px}.t3{left:450px}.t4{left:640px}
.site-footer{position:absolute;left:0;top:530px;width:866px;height:322px;background:var(--footer);color:var(--white)}
.footer-brand{position:absolute;left:83px;top:62px}
.footer-brand .dot{width:44px;height:44px;border-radius:50%;background:var(--white);margin-left:35px;margin-bottom:16px}
.footer-brand .brand-name{color:var(--white);font-size:21px;font-weight:500}
.footer-about{position:absolute;left:83px;top:165px;width:230px;font-size:8.6px;line-height:11.5px;font-weight:500}
.footer-heading{position:absolute;top:76px;font-size:14.5px;font-weight:500}
.contact-heading{left:336px}
.links-heading{left:631px}
.contact-item{position:absolute;font-size:10.5px;font-weight:500;padding-left:20px;line-height:16px}
.contact-item svg,.link-item svg{position:absolute;left:0;top:2px;width:13px;height:13px}
.contact-item span,.link-item span{display:block;color:var(--link);font-size:9.5px;font-weight:400}
.link-item{position:absolute;left:631px;font-size:10.5px;font-weight:500;line-height:16px}
.link-item b{font-weight:500;padding-left:27px}
.link-item span{margin-left:-2px;margin-top:5px}
.footer-rule{position:absolute;left:83px;top:270px;width:700px;height:1px;background:var(--rule)}
.copyright{position:absolute;left:0;top:291px;width:866px;padding-right:6px;text-align:center;font-family:"Noto Serif",serif;font-size:10.5px}
.version{position:absolute;right:13px;top:288px;font-size:11px}
</style>
</head>
<body>

<!-- Screen 1: service choice -->
<section class="screen screen--choice">
  <header class="site-header">
    <a class="portal-btn portal-btn--resellers">Resellers Portal</a>
    <a class="portal-btn portal-btn--customers">Customers Portal</a>
  </header>
  <div class="brand-badge"><span class="dot"></span><span class="brand-name">PanelBrite</span></div>
  <svg class="hero" viewBox="0 0 866 356" preserveAspectRatio="none">
    <defs>
      <linearGradient id="solarTones" x1="0" y1="0" x2="1" y2="1"><stop offset="0" stop-color="#9cc3e6"/><stop offset=".5" stop-color="#2a4f86"/><stop offset="1" stop-color="#5a6a48"/></linearGradient>
      <linearGradient id="gutterTones" x1="0" y1="0" x2="1" y2="1"><stop offset="0" stop-color="#6d7560"/><stop offset=".6" stop-color="#4d5147"/><stop offset="1" stop-color="#8a7a66"/></linearGradient>
    </defs>
    <polygon points="0,0 480,0 385,356 0,356" fill="url(#solarTones)" role="img" aria-label="Photo of a worker cleaning solar panels on a solar farm"/>
    <polygon points="480,0 866,0 866,356 385,356" fill="url(#gutterTones)" role="img" aria-label="Photo of a hand clearing leaves from a roof gutter"/>
    <line x1="480" y1="0" x2="385" y2="356" stroke="#f3a21b" stroke-width="4"/>
  </svg>
  <a class="choice-label choice-label--solar">Solar Panel Cleaning</a>
  <a class="choice-label choice-label--gutter">Gutter Cleaning</a>
  <footer class="site-footer" style="top:530px"></footer>
</section>

<!-- Screen 2: solar sectors -->
<section class="screen screen--solar">
  <header class="site-header">
    <a class="portal-btn portal-btn--resellers">Resellers Portal</a>
    <a class="portal-btn portal-btn--customers">Customers Portal</a>
  </header>
  <div class="brand-badge"><span class="dot"></span><span class="brand-name">PanelBrite</span></div>
  <svg class="hero" viewBox="0 0 866 443" preserveAspectRatio="none" style="height:443px" role="img" aria-label="Photo of a technician wiping rooftop solar panels">
    <defs><linearGradient id="solarRoof" x1="0" y1="0" x2="0" y2="1"><stop offset="0" stop-color="#3d6fb8"/><stop offset=".4" stop-color="#7d8ea0"/><stop offset=".7" stop-color="#23427a"/><stop offset="1" stop-color="#1b2f5c"/></linearGradient></defs>
    <rect width="866" height="443" fill="url(#solarRoof)"/>
  </svg>
  <p class="hero-copy hero-copy--title">Welcome to PanelBrite</p>
  <p class="hero-copy hero-copy--tagline">"Efficient, Safe &amp; Professional Solar Panel Cleaning"</p>
  <a class="sector-tile sector-tile--dark t1"><svg viewBox="0 0 40 40" fill="none" stroke="#fff" stroke-width="1.6"><path d="M4 14 20 5l16 9z"/><path d="M7 14v19M33 14v19M14 18v13M20 18v13M26 18v13M3 35h34"/></svg>Government</a>
  <a class="sector-tile sector-tile--light t2"><svg viewBox="0 0 40 40" fill="none" stroke="#fff" stroke-width="1.6"><circle cx="20" cy="24" r="10"/><path d="M12 18V5h5v9M20 14V3h5v11M28 18V8"/></svg>Infrastructure</a>
  <a class="sector-tile sector-tile--dark t3"><svg viewBox="0 0 40 40" fill="none" stroke="#fff" stroke-width="1.6"><path d="M6 36V12h12v24M18 36V4h16v32M3 36h34M10 17h4M10 23h4M10 29h4M23 10h6M23 17h6M23 24h6"/></svg>Commercial</a>
  <a class="sector-tile sector-tile--light t4"><svg viewBox="0 0 40 40" fill="none" stroke="#fff" stroke-width="1.6"><path d="M4 20 20 6l16 14M8 17v17h24V17M16 34v-9h8v9M28 8v6"/></svg>Residential</a>
  <footer class="site-footer"></footer>
</section>

<!-- Screen 3: gutter sectors -->
<section class="screen screen--gutter">
  <header class="site-header">
    <a class="portal-btn portal-btn--resellers">Resellers Portal</a>
    <a class="portal-btn portal-btn--customers">Customers Portal</a>
  </header>
  <div class="brand-badge"><span class="dot"></span><span class="brand-name">PanelBrite</span></div>
  <svg class="hero" viewBox="0 0 866 443" preserveAspectRatio="none" style="height:443px" role="img" aria-label="Photo of a man on a ladder clearing a tiled roof gutter">
    <defs><linearGradient id="gutterRoof" x1="0" y1="0" x2="1" y2="1"><stop offset="0" stop-color="#6a4a48"/><stop offset=".4" stop-color="#5b5d58"/><stop offset=".75" stop-color="#4c5a3e"/><stop offset="1" stop-color="#3b4a30"/></linearGradient></defs>
    <rect width="866" height="443" fill="url(#gutterRoof)"/>
  </svg>
  <p class="hero-copy hero-copy--title">Welcome to Gutter Cleaning</p>
  <p class="hero-copy hero-copy--tagline">"Safe &amp; Effective Gutter Cleaning for Homes &amp; Businesses"</p>
  <a class="sector-tile sector-tile--dark t1"><svg viewBox="0 0 40 40" fill="none" stroke="#fff" stroke-width="1.6"><path d="M4 14 20 5l16 9z"/><path d="M7 14v19M33 14v19M14 18v13M20 18v13M26 18v13M3 35h34"/></svg>Government</a>
  <a class="sector-tile sector-tile--light t2"><svg viewBox="0 0 40 40" fill="none" stroke="#fff" stroke-width="1.6"><path d="M8 36V4h24v32M4 36h32M13 9h4M23 9h4M13 16h4M23 16h4M13 23h4M23 23h4M17 36v-6h6v6"/></svg>Strata</a>
  <a class="sector-tile sector-tile--dark t3"><svg viewBox="0 0 40 40" fill="none" stroke="#fff" stroke-width="1.6"><path d="M6 36V12h12v24M18 36V4h16v32M3 36h34M10 17h4M10 23h4M10 29h4M23 10h6M23 17h6M23 24h6"/></svg>Commercial</a>
  <a class="sector-tile sector-tile--light t4"><svg viewBox="0 0 40 40" fill="none" stroke="#fff" stroke-width="1.6"><path d="M4 20 20 6l16 14M8 17v17h24V17M16 34v-9h8v9M28 8v6"/></svg>Residential</a>
  <footer class="site-footer"></footer>
</section>

<style>
/* footer content shared layout */
</style>

<!-- Footer content is written per screen below -->
<div style="display:none"></div>

<style>
.site-footer{display:block}
</style>

<template></template>

<style>
.screen .site-footer{top:530px}
.screen--choice .site-footer{top:530px}
</style>

<style>
.footer-content{position:absolute;inset:0}
</style>

<div class="footers">
  <div class="screen" style="top:641px;height:322px;background:var(--footer)">
    <div class="footer-content" style="color:var(--white)">
      <div class="footer-brand"><div class="dot"></div><div class="brand-name">PanelBrite</div></div>
      <p class="footer-about">Lorem Ipsum is simply dummy text of the printing and typesetting industry. Lorem Ipsum has been the industry's standard dummy text ever since the 1500s,</p>
      <h3 class="footer-heading contact-heading">Contact Us</h3>
      <p class="contact-item" style="left:338px;top:107px"><svg viewBox="0 0 16 16"><path d="M3 1l3 3-2 2c1 2 3 4 6 6l2-2 3 3-2 2C7 15 1 9 1 3z" fill="#fff"/></svg>Sydney<span>02 7391 5084</span></p>
      <p class="contact-item" style="left:473px;top:107px"><svg viewBox="0 0 16 16"><path d="M3 1l3 3-2 2c1 2 3 4 6 6l2-2 3 3-2 2C7 15 1 9 1 3z" fill="#fff"/></svg>Canberra<span>02 6178 3045</span></p>
      <p class="contact-item" style="left:338px;top:143px"><svg viewBox="0 0 16 16"><path d="M3 1l3 3-2 2c1 2 3 4 6 6l2-2 3 3-2 2C7 15 1 9 1 3z" fill="#fff"/></svg>Southern Highlands<span>02 4863 1507</span></p>
      <p class="contact-item" style="left:473px;top:143px"><svg viewBox="0 0 16 16"><path d="M3 1l3 3-2 2c1 2 3 4 6 6l2-2 3 3-2 2C7 15 1 9 1 3z" fill="#fff"/></svg>Wollongong<span>02 4239 7615</span></p>
      <p class="contact-item" style="left:338px;top:177px"><svg viewBox="0 0 16 16"><path d="M3 1l3 3-2 2c1 2 3 4 6 6l2-2 3 3-2 2C7 15 1 9 1 3z" fill="#fff"/></svg>Goulburn<span>02 4863 1507</span></p>
      <h3 class="footer-heading links-heading">Quick Links</h3>
      <p class="link-item" style="top:105px"><svg viewBox="0 0 16 16" style="width:16px"><rect x="1" y="3" width="14" height="10" fill="none" stroke="#fff" stroke-width="1.4"/><path d="M1 3l7 6 7-6" fill="none" stroke="#fff" stroke-width="1.4"/></svg><b>Mail</b><span>sales@panelbrite.com.au</span></p>
      <p class="link-item" style="top:149px"><svg viewBox="0 0 16 16" style="left:3px"><path d="M8 1a5 5 0 0 1 5 5c0 4-5 9-5 9S3 10 3 6a5 5 0 0 1 5-5z" fill="none" stroke="#fff" stroke-width="1.4"/><circle cx="8" cy="6" r="2" fill="#fff"/></svg><b>Head Office</b><span>sales@panelbrite.com.au</span></p>
      <p class="link-item" style="top:190px"><svg viewBox="0 0 16 16" style="left:2px"><path d="M2 15V5h5v10M7 15V2h7v13M1 15h14M4 8h1M4 11h1M9 5h3M9 8h3M9 11h3" fill="none" stroke="#fff" stroke-width="1.2"/></svg><b>ABN</b><span>sales@panelbrite.com.au</span></p>
      <div class="footer-rule"></div>
      <p class="copyright">Copyright © 2025 panelbrite. All Rights Reserved.</p>
      <p class="version">C81</p>
    </div>
  </div>
  <div class="screen" style="top:1547px;height:322px;background:var(--footer)">
    <div class="footer-content" style="color:var(--white)">
      <div class="footer-brand"><div class="dot"></div><div class="brand-name">PanelBrite</div></div>
      <p class="footer-about">Lorem Ipsum is simply dummy text of the printing and typesetting industry. Lorem Ipsum has been the industry's standard dummy text ever since the 1500s,</p>
      <h3 class="footer-heading contact-heading">Contact Us</h3>
      <p class="contact-item" style="left:338px;top:107px"><svg viewBox="0 0 16 16"><path d="M3 1l3 3-2 2c1 2 3 4 6 6l2-2 3 3-2 2C7 15 1 9 1 3z" fill="#fff"/></svg>Sydney<span>02 7391 5084</span></p>
      <p class="contact-item" style="left:473px;top:107px"><svg viewBox="0 0 16 16"><path d="M3 1l3 3-2 2c1 2 3 4 6 6l2-2 3 3-2 2C7 15 1 9 1 3z" fill="#fff"/></svg>Canberra<span>02 6178 3045</span></p>
      <p class="contact-item" style="left:338px;top:143px"><svg viewBox="0 0 16 16"><path d="M3 1l3 3-2 2c1 2 3 4 6 6l2-2 3 3-2 2C7 15 1 9 1 3z" fill="#fff"/></svg>Southern Highlands<span>02 4863 1507</span></p>
      <p class="contact-item" style="left:473px;top:143px"><svg viewBox="0 0 16 16"><path d="M3 1l3 3-2 2c1 2 3 4 6 6l2-2 3 3-2 2C7 15 1 9 1 3z" fill="#fff"/></svg>Wollongong<span>02 4239 7615</span></p>
      <p class="contact-item" style="left:338px;top:177px"><svg viewBox="0 0 16 16"><path d="M3 1l3 3-2 2c1 2 3 4 6 6l2-2 3 3-2 2C7 15 1 9 1 3z" fill="#fff"/></svg>Goulburn<span>02 4863 1507</span></p>
      <h3 class="footer-heading links-heading">Quick Links</h3>
      <p class="link-item" style="top:105px"><svg viewBox="0 0 16 16" style="width:16px"><rect x="1" y="3" width="14" height="10" fill="none" stroke="#fff" stroke-width="1.4"/><path d="M1 3l7 6 7-6" fill="none" stroke="#fff" stroke-width="1.4"/></svg><b>Mail</b><span>sales@panelbrite.com.au</span></p>
      <p class="link-item" style="top:149px"><svg viewBox="0 0 16 16" style="left:3px"><path d="M8 1a5 5 0 0 1 5 5c0 4-5 9-5 9S3 10 3 6a5 5 0 0 1 5-5z" fill="none" stroke="#fff" stroke-width="1.4"/><circle cx="8" cy="6" r="2" fill="#fff"/></svg><b>Head Office</b><span>sales@panelbrite.com.au</span></p>
      <p class="link-item" style="top:190px"><svg viewBox="0 0 16 16" style="left:2px"><path d="M2 15V5h5v10M7 15V2h7v13M1 15h14M4 8h1M4 11h1M9 5h3M9 8h3M9 11h3" fill="none" stroke="#fff" stroke-width="1.2"/></svg><b>ABN</b><span>sales@panelbrite.com.au</span></p>
      <div class="footer-rule"></div>
      <p class="copyright">Copyright © 2025 panelbrite. All Rights Reserved.</p>
      <p class="version">C81</p>
    </div>
  </div>
  <div class="screen" style="top:2483px;height:322px;background:var(--footer)">
    <div class="footer-content" style="color:var(--white)">
      <div class="footer-brand"><div class="dot"></div><div class="brand-name">PanelBrite</div></div>
      <p class="footer-about">Lorem Ipsum is simply dummy text of the printing and typesetting industry. Lorem Ipsum has been the industry's standard dummy text ever since the 1500s,</p>
      <h3 class="footer-heading contact-heading">Contact Us</h3>
      <p class="contact-item" style="left:338px;top:107px"><svg viewBox="0 0 16 16"><path d="M3 1l3 3-2 2c1 2 3 4 6 6l2-2 3 3-2 2C7 15 1 9 1 3z" fill="#fff"/></svg>Sydney<span>02 7391 5084</span></p>
      <p class="contact-item" style="left:473px;top:107px"><svg viewBox="0 0 16 16"><path d="M3 1l3 3-2 2c1 2 3 4 6 6l2-2 3 3-2 2C7 15 1 9 1 3z" fill="#fff"/></svg>Canberra<span>02 6178 3045</span></p>
      <p class="contact-item" style="left:338px;top:143px"><svg viewBox="0 0 16 16"><path d="M3 1l3 3-2 2c1 2 3 4 6 6l2-2 3 3-2 2C7 15 1 9 1 3z" fill="#fff"/></svg>Southern Highlands<span>02 4863 1507</span></p>
      <p class="contact-item" style="left:473px;top:143px"><svg viewBox="0 0 16 16"><path d="M3 1l3 3-2 2c1 2 3 4 6 6l2-2 3 3-2 2C7 15 1 9 1 3z" fill="#fff"/></svg>Wollongong<span>02 4239 7615</span></p>
      <p class="contact-item" style="left:338px;top:177px"><svg viewBox="0 0 16 16"><path d="M3 1l3 3-2 2c1 2 3 4 6 6l2-2 3 3-2 2C7 15 1 9 1 3z" fill="#fff"/></svg>Goulburn<span>02 4863 1507</span></p>
      <h3 class="footer-heading links-heading">Quick Links</h3>
      <p class="link-item" style="top:105px"><svg viewBox="0 0 16 16" style="width:16px"><rect x="1" y="3" width="14" height="10" fill="none" stroke="#fff" stroke-width="1.4"/><path d="M1 3l7 6 7-6" fill="none" stroke="#fff" stroke-width="1.4"/></svg><b>Mail</b><span>sales@panelbrite.com.au</span></p>
      <p class="link-item" style="top:149px"><svg viewBox="0 0 16 16" style="left:3px"><path d="M8 1a5 5 0 0 1 5 5c0 4-5 9-5 9S3 10 3 6a5 5 0 0 1 5-5z" fill="none" stroke="#fff" stroke-width="1.4"/><circle cx="8" cy="6" r="2" fill="#fff"/></svg><b>Head Office</b><span>sales@panelbrite.com.au</span></p>
      <p class="link-item" style="top:190px"><svg viewBox="0 0 16 16" style="left:2px"><path d="M2 15V5h5v10M7 15V2h7v13M1 15h14M4 8h1M4 11h1M9 5h3M9 8h3M9 11h3" fill="none" stroke="#fff" stroke-width="1.2"/></svg><b>ABN</b><span>sales@panelbrite.com.au</span></p>
      <div class="footer-rule"></div>
      <p class="copyright">Copyright © 2025 panelbrite. All Rights Reserved.</p>
      <p class="version">C81</p>
    </div>
  </div>
</div>

</body>
</html>
```